Dental Business Card

I need Dental oriented business cards.
On the front side -
- on the first line, my name:
Dr Marlo Vintner
- on the second line (just underneath):
Doctor of Dental Medicine
- on the third line, or underneath that or in a corner, I would like the address and phone number:
5182 Ch. Birchfield
Montreal QC H2T 4B9
514-629-5074
- other than that i would maybe like a logo of a tooth, but i want it to be subtle and very basic!
- I would like the card to be preferably black or dark grey-ish with the writing in white
On the other side -
- 2-3 lines with the possibility to write the next appointment the box with the lines should be white, with the rest of the card being black

```html
<!DOCTYPE html>
<html lang="en">
<head>
<meta charset="utf-8">
<title>Dr Marlo Vintner – Business Card</title>
<link rel="stylesheet" href="https://fonts.googleapis.com/css2?family=Montserrat:wght@400;500;600&family=Open+Sans:ital,wght@0,400;1,400&display=swap">
<style>
  :root {
    --page-bg: #3a3b3e;
    --card-dark: #2b2c2f;
    --card-dark-edge: #202124;
    --text-white: #ffffff;
    --text-soft: #d4d6da;
    --text-muted: #aeb1b6;
    --rule: #8a8d92;
    --box-white: #ffffff;
    --box-line: #c9cbce;
  }
  * { margin: 0; padding: 0; box-sizing: border-box; }
  html, body {
    width: 1200px; height: 933px; overflow: hidden;
    background: var(--page-bg);
  }
  .canvas {
    position: relative; width: 1200px; height: 933px;
  }
  .card {
    position: absolute; left: 250px; width: 700px; height: 400px;
    background: linear-gradient(135deg, var(--card-dark) 0%, #36373b 55%, var(--card-dark-edge) 100%);
    box-shadow: 0 10px 24px rgba(0,0,0,0.35);
    overflow: hidden;
  }
  .card--front { top: 50px; }
  .card--back { top: 483px; }

  /* Front */
  .brand {
    position: absolute; top: 52px; left: 0; right: 0;
    display: flex; align-items: center; justify-content: center; gap: 10px;
    font-family: "Montserrat", sans-serif; font-weight: 500;
    font-size: 15px; letter-spacing: 4px; text-transform: uppercase;
    color: var(--text-white);
  }
  .brand__dot {
    width: 12px; height: 12px; border-radius: 50%;
    background: var(--text-white);
  }
  .identity {
    position: absolute; top: 122px; left: 0; right: 0; text-align: center;
  }
  .identity__name {
    font-family: "Montserrat", sans-serif; font-weight: 600;
    font-size: 38px; letter-spacing: 5px; text-transform: uppercase;
    color: var(--text-white);
  }
  .identity__title {
    margin-top: 6px;
    font-family: "Montserrat", sans-serif; font-weight: 400;
    font-size: 16px; letter-spacing: 5px; text-transform: uppercase;
    color: var(--text-soft);
  }
  .divider {
    position: absolute; top: 226px; left: 60px; right: 60px;
    height: 1px; background: var(--rule);
  }
  .contact {
    position: absolute; top: 252px; left: 0; right: 0; text-align: center;
    font-family: "Open Sans", sans-serif; font-size: 17px;
    color: var(--text-soft); line-height: 1.9;
  }
  .contact__sep { color: var(--rule); padding: 0 10px; }

  /* Back */
  .appointment__label {
    position: absolute; top: 30px; right: 48px;
    font-family: "Montserrat", sans-serif; font-weight: 500;
    font-size: 22px; letter-spacing: 6px; text-transform: uppercase;
    color: var(--text-soft);
  }
  .appointment__box {
    position: absolute; top: 76px; left: 48px; right: 48px; height: 200px;
    background: var(--box-white);
    padding: 44px 40px 0;
  }
  .appointment__line {
    height: 1px; background: var(--box-line); margin-bottom: 48px;
  }
  .appointment__note {
    position: absolute; left: 48px; top: 300px;
    font-family: "Open Sans", sans-serif; font-style: italic;
    font-size: 15px; line-height: 1.6; color: var(--text-muted);
  }
</style>
</head>
<body>
<main class="canvas">
  <section class="card card--front" aria-label="Business card front">
    <div class="brand"><span class="brand__dot"></span>Vintner Dental</div>
    <div class="identity">
      <h1 class="identity__name">Dr Marlo Vintner</h1>
      <p class="identity__title">Doctor of Dental Medicine</p>
    </div>
    <div class="divider"></div>
    <address class="contact" style="font-style:normal">
      <div>5182 Ch. Birchfield<span class="contact__sep">|</span>Montreal QC H2T 4B9</div>
      <div>514 - 629 - 5074</div>
    </address>
  </section>

  <section class="card card--back" aria-label="Business card back">
    <h2 class="appointment__label">Appointment</h2>
    <div class="appointment__box">
      <div class="appointment__line"></div>
      <div class="appointment__line"></div>
      <div class="appointment__line"></div>
    </div>
    <p class="appointment__note">If you are unable to keep your appointment,<br>please contact us as soon as possible.</p>
  </section>
</main>
</body>
</html>
```